Demolition Company Billboard Design 13 feet wide 15 feet high

This is my first billboard on a busy road. I want it to be professional but with some eye catching flair that matches by business which is a demoltion business and also list my services. My company slogan is also

"call quill to clear the hill"

Target Market(s)

Home Ownerd and General Construction Companies

Industry/Entity Type

construction

Colors
0054AA
0677BA
7BADD7
CADEEF
E8F1F8

Requirements
Must have
• My services listed in the pictures my website and my phone number

```html
<!DOCTYPE html>
<html lang="en">
<head>
<meta charset="utf-8">
<title>Quill Demolition Billboard</title>
<link rel="stylesheet" href="https://fonts.googleapis.com/css2?family=Montserrat:ital,wght@0,400;0,500;0,700;1,500&display=swap">
<style>
  :root {
    --page: #8a8a8a;
    --paper: #ffffff;
    --ink: #1e1e1e;
    --navy: #1f4870;
    --on-navy: #ffffff;
  }
  * { margin: 0; padding: 0; box-sizing: border-box; }
  html, body {
    width: 1199px;
    height: 1200px;
    overflow: hidden;
    background: var(--page);
    font-family: "Montserrat", sans-serif;
  }
  .billboard {
    position: absolute;
    left: 80px;
    top: 0;
    width: 1040px;
    height: 1200px;
    background: var(--paper);
    text-align: center;
  }
  .slogan {
    position: absolute;
    top: 102px;
    left: 0;
    right: 0;
    font-style: italic;
    font-weight: 500;
    font-size: 56px;
    letter-spacing: 0.5px;
    color: var(--ink);
    text-transform: uppercase;
  }
  .brand-name {
    position: absolute;
    top: 340px;
    left: 0;
    right: 0;
    font-weight: 500;
    font-size: 88px;
    color: var(--ink);
    letter-spacing: 1px;
  }
  .info-band {
    position: absolute;
    left: 0;
    top: 612px;
    width: 100%;
    height: 588px;
    background: var(--navy);
    color: var(--on-navy);
  }
  .services {
    position: absolute;
    top: 70px;
    left: 0;
    right: 0;
    font-weight: 700;
    font-size: 68px;
    line-height: 88px;
    letter-spacing: 1px;
    text-transform: uppercase;
  }
  .divider {
    position: absolute;
    top: 302px;
    left: 250px;
    width: 540px;
    height: 2px;
    background: var(--on-navy);
  }
  .phone {
    position: absolute;
    top: 352px;
    left: 0;
    right: 0;
    font-weight: 700;
    font-size: 54px;
    letter-spacing: 1px;
  }
  .website {
    position: absolute;
    top: 420px;
    left: 0;
    right: 0;
    font-weight: 400;
    font-size: 60px;
    letter-spacing: 0.5px;
  }
</style>
</head>
<body>
  <main class="billboard">
    <p class="slogan">Call Quill to Clear the Hill</p>
    <p class="brand-name">Quill Demolition</p>
    <section class="info-band">
      <p class="services">Interior • Exterior<br>Commercial</p>
      <div class="divider"></div>
      <p class="phone">412-555-0187</p>
      <p class="website">www.quilldemolition.com</p>
    </section>
  </main>
</body>
</html>
```